Dr. Pell Works
Business card, stationary, fax page, envelope
Dr. Pell Works - Corporate Services
Creative Brief
Bright & Fun-filled
Grant Bevis Hallworth
Senior Account Executive
417 S. Tavish Ave Los Angeles CA 90012
grant@drpellworks.example
drpellworks.example
I also have 4 other people that need their won business cards but with their cell phone and title info.

```html
<!DOCTYPE html>
<html lang="en">
<head>
<meta charset="utf-8">
<title>Dr. Pell Works — Business Card</title>
<link rel="stylesheet" href="https://fonts.googleapis.com/css2?family=Roboto+Condensed:wght@700&family=Open+Sans:wght@400;600&display=swap">
<style>
  :root {
    --backdrop: #e8e3dc;
    --card-dark: #231f20;
    --brand-yellow: #f7c600;
    --pattern-yellow: #fbd63a;
    --ink: #231f20;
    --white: #ffffff;
    --muted-rule: #8a7400;
  }
  html, body {
    margin: 0;
    padding: 0;
    width: 1200px;
    height: 961px;
    overflow: hidden;
    background: var(--backdrop);
  }
  .canvas {
    position: relative;
    width: 1200px;
    height: 961px;
  }
  .card {
    position: absolute;
    width: 563px;
    height: 319px;
    border-radius: 16px;
    overflow: hidden;
    box-shadow: 0 6px 18px rgba(0,0,0,0.22);
  }
  /* Front */
  .card-front {
    left: 117px;
    top: 143px;
    background: var(--card-dark);
  }
  .brand {
    position: absolute;
    display: flex;
    align-items: center;
  }
  .brand-mark {
    border-radius: 50%;
    flex: none;
  }
  .brand-name {
    font-family: "Roboto Condensed", "Arial Narrow", sans-serif;
    font-weight: 700;
    line-height: 0.95;
    margin: 0;
  }
  .card-front .brand {
    left: 36px;
    top: 28px;
  }
  .card-front .brand-mark {
    width: 112px;
    height: 112px;
    background: var(--brand-yellow);
    margin-right: 26px;
  }
  .card-front .brand-name {
    font-size: 64px;
    color: var(--white);
  }
  .holder {
    position: absolute;
    left: 92px;
    top: 186px;
    display: flex;
    align-items: baseline;
    white-space: nowrap;
  }
  .holder-name {
    font-family: "Roboto Condensed", "Arial Narrow", sans-serif;
    font-weight: 700;
    font-size: 25px;
    color: var(--white);
  }
  .holder-rule {
    width: 2px;
    height: 24px;
    background: var(--white);
    margin: 0 10px;
    align-self: center;
  }
  .holder-title {
    font-family: "Open Sans", Arial, sans-serif;
    font-weight: 600;
    font-size: 14px;
    color: var(--brand-yellow);
  }
  .contact-band {
    position: absolute;
    left: 0;
    right: 0;
    bottom: 0;
    height: 80px;
    background: var(--brand-yellow);
    display: flex;
    align-items: center;
    padding-left: 20px;
    box-sizing: border-box;
    font-family: "Open Sans", Arial, sans-serif;
    font-size: 12.5px;
    line-height: 1.45;
    color: var(--ink);
  }
  .contact-col { padding: 0 16px; }
  .contact-col:first-child { padding-left: 0; width: 150px; }
  .contact-col + .contact-col { border-left: 1px solid var(--muted-rule); }
  .contact-col b { font-weight: 600; }
  /* Back */
  .card-back {
    left: 512px;
    top: 514px;
  }
  .back-field {
    position: absolute;
    inset: 0;
    background: linear-gradient(135deg, var(--pattern-yellow) 0%, var(--brand-yellow) 45%, var(--pattern-yellow) 100%);
  }
  .card-back .brand {
    left: 86px;
    top: 78px;
  }
  .card-back .brand-mark {
    width: 118px;
    height: 118px;
    background: var(--card-dark);
    margin-right: 22px;
  }
  .card-back .brand-name {
    font-size: 76px;
    color: var(--ink);
  }
  .website {
    position: absolute;
    right: 110px;
    bottom: 28px;
    font-family: "Open Sans", Arial, sans-serif;
    font-weight: 600;
    font-size: 15px;
    color: var(--ink);
  }
</style>
</head>
<body>
<main class="canvas">

  <section class="card card-front" aria-label="Business card front">
    <div class="brand">
      <div class="brand-mark"></div>
      <p class="brand-name">Dr. Pell<br>Works</p>
    </div>
    <div class="holder">
      <span class="holder-name">Grant Bevis Hallworth</span>
      <span class="holder-rule"></span>
      <span class="holder-title">Senior Account Executive</span>
    </div>
    <div class="contact-band">
      <div class="contact-col">417 S. Tavish Ave<br>Los Angeles CA 90012</div>
      <div class="contact-col"><b>P :</b> 323-555-0148<br><b>C :</b> 310-555-0172<br><b>F :</b> 323-555-0193</div>
      <div class="contact-col"><b>E :</b> grant@drpellworks.example<br><b>W :</b> www.drpellworks.example</div>
    </div>
  </section>

  <section class="card card-back" aria-label="Business card back">
    <div class="back-field" role="img" aria-label="Faint yellow geometric pattern of scattered quarter-circle shapes"></div>
    <div class="brand">
      <div class="brand-mark"></div>
      <p class="brand-name">Dr. Pell<br>Works</p>
    </div>
    <div class="website">www.drpellworks.example</div>
  </section>

</main>
</body>
</html>
```